Flyer Design for catering company "Rosemary's Larder"

We need a flyer design for a small catering company based in Melbourne, Australia called Rosemary's Larder. We are in the process of re-branding at the moment and want to use the new brand for the logo. The new website is still under development but you can have a look at it here: http://rosemaryslarder.sitevane.net/minimal-layout The product we want to market i the flyer are our ready-made meals. We are marketing to the corporate world. The meals are intended to be purchased by large firms to feed their staff that are working back late after-hours. They are home-made, fresh, healthy, convenient and most importantly - delicious! You can find the menu and a brief explanation of the ready-made meals on the website. I thought that we might include the menu on the backside of the flyer but i am not set on this.

We want to provide an introductory offer of 10 meals for $100 (usually $130).

I have attached an image of where i got to with the flyer just for your information. You can see why i need your assistance!

I should also add that the logo is intended to be printed in a gold foil! Added Wednesday, February 3, 2016

Target Market(s)

Corporate market - this doesnt mean boring though. It wont be the big bosses who read this flyer it will be the catering managers - they are likely to see a lot of flyers so this one needs to stand out.

Industry/Entity Type

Catering

Requirements
Must have
• Must have the logo! Keep in mind the logo will be printed in a gold foil so it will be very metallic.
• Must reference introductory offer of 10 meals for $100.
• Must have website.
Nice to have
• Would like to see the menu on the backside - i am flexible with this if you have a better idea.
Should not have
• no cartoony images

```html
<!DOCTYPE html>
<html lang="en">
<head>
<meta charset="utf-8">
<title>Rosemary's Larder – Traditional Dishes Flyer</title>
<link href="https://fonts.googleapis.com/css2?family=Lobster&family=Lato:wght@400;700&family=Oswald:wght@500;600&display=swap" rel="stylesheet">
<style>
  :root {
    --gold: #b89c3a;
    --gold-light: #c9ad4c;
    --charcoal: #333333;
    --ink: #222222;
    --paper: #ffffff;
  }
  * { box-sizing: border-box; margin: 0; padding: 0; }
  html, body {
    width: 907px; height: 1200px; overflow: hidden;
    background: var(--paper);
    font-family: "Lato", Arial, sans-serif;
  }
  .flyer { position: relative; width: 907px; height: 1200px; overflow: hidden; background: var(--paper); }

  .hero-photo {
    position: absolute; left: 0; top: 0; width: 907px; height: 480px;
    background:
      linear-gradient(90deg, rgba(255,255,255,0) 0%, rgba(255,255,255,0) 58%, rgba(255,255,255,0.85) 72%, #fff 80%),
      linear-gradient(180deg, #6f8a5a 0%, #9a8468 20%, #b59a7c 45%, #d8cbb8 75%, #e9e2d6 100%);
  }
  .shapes { position: absolute; left: 0; top: 0; }

  .brand-seal {
    position: absolute; left: 692px; top: 102px; width: 154px; height: 154px;
    border-radius: 50%;
    background: radial-gradient(circle at 35% 30%, var(--gold-light), var(--gold) 70%);
    display: flex; align-items: center; justify-content: center; text-align: center;
  }
  .brand-seal .brand-name {
    color: var(--paper); font-family: "Lato", Arial, sans-serif; font-weight: 700;
    font-size: 22px; line-height: 1.2;
  }

  .offer-badge {
    position: absolute; left: 12px; top: 300px; width: 240px; height: 240px;
    border-radius: 50%; background: var(--charcoal);
    border: 8px solid var(--gold);
    display: flex; flex-direction: column; align-items: center; justify-content: center;
    text-align: center;
  }
  .offer-badge .offer-count { font-family: "Oswald", Arial, sans-serif; font-weight: 500; color: var(--gold-light); font-size: 34px; line-height: 1; }
  .offer-badge .offer-for { font-family: "Lobster", cursive; color: var(--gold-light); font-size: 40px; line-height: 1.15; }
  .offer-badge .offer-price { font-family: "Oswald", Arial, sans-serif; font-weight: 600; color: var(--paper); font-size: 58px; line-height: 1; }

  .headline { position: absolute; right: 60px; top: 512px; text-align right; text-align: right; font-family: "Lobster", cursive; font-weight: 400; line-height: 0.95; }
  .headline .line-1 { display: block; color: var(--gold); font-size: 84px; }
  .headline .line-2 { display: block; color: var(--charcoal); font-size: 84px; }

  .menu-left { position: absolute; left: 30px; top: 700px; width: 400px; color: var(--paper); }
  .menu-left .dish { margin-bottom: 20px; }
  .menu-left .dish-name { font-family: "Lobster", cursive; color: var(--ink); font-size: 28px; font-weight: 400; margin-bottom: 8px; }
  .menu-left .dish-desc { font-size: 17px; line-height: 1.3; }

  .menu-right { position: absolute; right: 0; top: 690px; width: 360px; }
  .menu-right .dish { margin-bottom: 24px; }
  .menu-right .dish-name {
    display: block; margin-left: auto; width: 330px; height: 42px;
    background: linear-gradient(180deg, var(--gold-light), var(--gold));
    border-radius: 22px 0 0 22px;
    font-family: "Lobster", cursive; font-weight: 400; font-size: 26px; color: var(--ink);
    padding: 4px 0 0 24px; margin-bottom: 18px;
  }
  .menu-right .dish-desc {
    font-size: 20px; line-height: 1.3; color: var(--ink); text-align: right; padding-right: 24px;
  }
  .menu-right .dish:last-child .dish-desc { margin-left: -80px; }

  .visit { position: absolute; left: 0; top: 0; width: 907px; text-align: center; }
  .visit .visit-label { position: absolute; top: 1036px; width: 100%; font-family: "Lobster", cursive; color: var(--gold); font-size: 40px; line-height: 1.2; }
  .visit .visit-url { position: absolute; top: 1140px; width: 100%; color: var(--paper); font-size: 20px; letter-spacing: 5px; }
</style>
</head>
<body>
<main class="flyer">
  <div class="hero-photo" role="img" aria-label="Photo of a waitress in a white shirt and black vest holding a platter of food in a restaurant"></div>

  <svg class="shapes" width="907" height="1200" viewBox="0 0 907 1200" aria-hidden="true">
    <path d="M0,400 C300,372 650,380 907,452 L907,1200 L0,1200 Z" fill="var(--charcoal)"/>
    <path d="M0,432 C300,406 650,414 907,486 L907,1200 L0,1200 Z" fill="var(--gold)"/>
    <path d="M0,439 C300,414 650,422 907,494 L907,1200 L0,1200 Z" fill="var(--paper)"/>
    <path d="M0,452 C300,428 650,436 907,506 L907,1200 L0,1200 Z" fill="var(--gold)"/>
    <path d="M0,463 C300,440 650,448 907,516 L907,1200 L0,1200 Z" fill="var(--paper)"/>
    <path d="M0,638 C300,630 540,790 640,1200 L0,1200 Z" fill="var(--gold)"/>
    <path d="M0,650 C295,644 525,800 622,1200 L0,1200 Z" fill="var(--paper)"/>
    <path d="M0,658 C290,652 515,806 608,1200 L0,1200 Z" fill="var(--charcoal)"/>
    <path d="M0,676 C280,672 495,818 585,1200 L0,1200 Z" fill="var(--gold)"/>
    <path d="M0,1032 C300,1014 620,1020 907,1040 L907,1200 L0,1200 Z" fill="var(--paper)"/>
    <path d="M0,1100 C300,1082 620,1082 907,1098 L907,1200 L0,1200 Z" fill="var(--gold)"/>
    <path d="M0,1110 C300,1092 620,1092 907,1108 L907,1200 L0,1200 Z" fill="var(--charcoal)"/>
  </svg>

  <div class="brand-seal"><span class="brand-name">Rosemary's<br>Larder</span></div>

  <div class="offer-badge">
    <span class="offer-count">10 MEALS</span>
    <span class="offer-for">for</span>
    <span class="offer-price">$100</span>
  </div>

  <h1 class="headline"><span class="line-1">Traditional</span><span class="line-2">Dishes</span></h1>

  <section class="menu-left">
    <div class="dish">
      <h2 class="dish-name">Traditional lasagne</h2>
      <p class="dish-desc">Beef lasagne with a creamy<br>béchamel sauce</p>
    </div>
    <div class="dish">
      <h2 class="dish-name">Pork and veal meatballs</h2>
      <p class="dish-desc">Pork &amp; veal meatballs in a rich<br>tomato passata with risoni<br>&amp; green beans</p>
    </div>
    <div class="dish">
      <h2 class="dish-name">Thai red beef curry</h2>
      <p class="dish-desc">Slow cooked red beef curry with basmati rice</p>
    </div>
  </section>

  <section class="menu-right">
    <div class="dish">
      <h2 class="dish-name">Chicken risotto</h2>
      <p class="dish-desc">Traditional risotto made with<br>chicken, fresh vegetables<br>and Arborio rice</p>
    </div>
    <div class="dish">
      <h2 class="dish-name">Shepherd's pie</h2>
      <p class="dish-desc">A low carb version of the classic<br>British dish made with minced<br>lamb and covered with a<br>delicious sweet potato<br>and potato mash</p>
    </div>
  </section>

  <footer class="visit">
    <p class="visit-label">Visit us</p>
    <p class="visit-url">www.rosemaryslarder.sitevane.net</p>
  </footer>
</main>
</body>
</html>
```